Lumo Lodge Brochure Design

Hotel / Spa well resort brochure in A4 size. We provide content ( for 12 pages ), 40 + pictures. Resort is under renovation to a yoga, meditation, wellness concept . New look pictures are not available. We have to present old pics and some design pics in a way to create anticipation and confidence in new resort.
Content files are attached.
Also, to see online, Current Design is at http://www.velmora.example/brochure/ This design is NOT ACCEPTABLE and we are looking for a more elegant design which suits the concept.
Content Files are at http://shortlnk.example/velmoratext
Tables/ price lists: http://shortlnk.example/ratesvel
Pictures ( to be used selectively as resort is undergoing renovations and these pictures will not be 100% valid after renovations) http://shortlnk.example/velmoraphotos
Pictures of Our Area
http://shortlnk.example/tovrinzone
Other Pictures:
http://shortlnk.example/fullresvelmora
http://shortlnk.example/velmoraglossy
http://shortlnk.example/posesatvelmora
Link to Tarvo Map and birds eye view images. http://mapviewr.example/K4RW2p
Link to Plixa Maps for earth and pictures images http://locatr.example/maps/qBTZW
Target Market(s)
Travel Industry Professionals, Travel Agents
Industry/Entity Type
Hotel
Look and feel

```html
<!DOCTYPE html>
<html lang="en">
<head>
<meta charset="utf-8">
<title>Lumo Lodge Brochure Spread</title>
<link href="https://fonts.googleapis.com/css2?family=Cormorant+Garamond:wght@500;600&family=Source+Sans+3:ital,wght@0,400;0,700;1,700&display=swap" rel="stylesheet">
<style>
  :root {
    --backdrop: #2a2a2a;
    --paper: #ffffff;
    --brown: #5a2412;
    --rust: #b5432a;
    --text: #3a3a3a;
    --sky-top: #5e96d6;
    --sky-low: #b9d4ee;
    --sea: #1f7fb8;
    --pine: #4d6b34;
    --haze: #e6ecf1;
    --skin: #d9a78a;
  }
  * { margin: 0; padding: 0; box-sizing: border-box; }
  html, body { width: 1200px; height: 817px; overflow: hidden; background: var(--backdrop); }
  .spread {
    position: absolute; left: 64px; top: 29px; width: 1073px; height: 758px;
    background: var(--paper); display: flex;
  }
  .page { position: relative; width: 50%; height: 100%; overflow: hidden; }

  .brand { text-align: center; color: var(--brown); }
  .brand-name {
    font-family: "Source Sans 3", sans-serif; font-weight: 700;
    font-size: 52px; letter-spacing: 1px; line-height: 1;
  }
  .brand-tagline {
    font-family: "Source Sans 3", sans-serif; font-style: italic; font-weight: 700;
    font-size: 11.5px; color: #111; margin-top: 14px;
  }

  .back .brand { position: absolute; top: 232px; left: 0; right: 0; }
  .contact {
    position: absolute; top: 352px; left: 0; right: 0; text-align: center;
    font-family: "Source Sans 3", sans-serif; font-size: 14px; line-height: 18px; color: var(--text);
  }
  .contact p { margin-bottom: 9px; }
  .back-photo {
    position: absolute; left: 0; right: 0; bottom: 0; height: 210px;
    background: linear-gradient(180deg, #f4f7fa 0%, var(--haze) 45%, #5f8fb0 58%, #3f6f93 80%, #6b7a5a 100%);
  }

  .cover-photo {
    position: absolute; left: 0; top: 0; width: 100%; height: 433px;
    background: linear-gradient(180deg, var(--sky-top) 0%, var(--sky-low) 55%, var(--sea) 64%, #2a93c4 82%, var(--pine) 100%);
  }
  .cover-headline {
    position: absolute; left: 19px; top: 14px; color: #fff;
    font-family: "Cormorant Garamond", serif; font-weight: 600; font-variant: small-caps;
    text-shadow: 0 1px 3px rgba(0,0,0,.35); line-height: 1.2;
  }
  .cover-headline .l1 { font-size: 23px; letter-spacing: .5px; }
  .cover-headline .l2 { font-size: 17px; }
  .cover-headline .l3 { font-size: 25px; margin-top: 4px; }
  .cover-headline .l4 { font-size: 19px; margin-top: 4px; }
  .cover-headline .l4 big { font-size: 32px; }
  .cover-headline .l5 { font-size: 15px; margin-top: 6px; }
  .cover-headline .l6 { font-size: 19px; margin-top: 6px; }
  .cover-headline .l7 { font-size: 19px; margin-top: 6px; }

  .rule { position: absolute; left: 0; right: 0; top: 439px; height: 8px; background: var(--rust); }
  .cover .brand { position: absolute; left: 10px; width: 250px; top: 590px; top: 560px; }
  .cover .brand-name { font-size: 50px; }
  .yoga-photo {
    position: absolute; right: 0; top: 528px; width: 290px; height: 230px;
    background: radial-gradient(ellipse at 55% 55%, var(--skin) 0%, #e8d6cb 45%, #ffffff 75%);
  }
  .visit-bar {
    position: absolute; left: 0; right: 0; bottom: 0; height: 40px; background: var(--rust);
    color: #fff; font-family: "Source Sans 3", sans-serif; font-weight: 700; font-size: 21px;
    line-height: 40px; padding-left: 18px;
  }
</style>
</head>
<body>
  <main class="spread">
    <section class="page back">
      <div class="brand">
        <div class="brand-name">Lumo Lodge</div>
        <div class="brand-tagline">Yoga - Meditation - Wellness</div>
      </div>
      <div class="contact">
        <p>Corran village Tessa<br>Vendra Bay<br>Marelia P.O. Box 40217</p>
        <p>Email :<br>booking@lumolodge.example</p>
        <p>+000-55-410021<br>+000-55-410022<br>+ 000-55-410023</p>
        <p>Fax : 00-000-55-410090</p>
        <p>www.lumolodge.example</p>
      </div>
      <div class="back-photo" role="img" aria-label="Hazy coastal view of calm blue sea below a rocky headland and dirt path"></div>
    </section>

    <section class="page cover">
      <div class="cover-photo" role="img" aria-label="Turquoise sea seen from a rocky coast framed by pine branches under a blue sky"></div>
      <h1 class="cover-headline">
        <div class="l1">Lumo Yoga Meditation</div>
        <div class="l2">and Wellness resort with</div>
        <div class="l3">UXURY SPA &amp; Beach</div>
        <div class="l4">holiday<big>OFFERS</big></div>
        <div class="l5">a selection of breaks Designed to</div>
        <div class="l6">Relax, Rejuvenate and</div>
        <div class="l7">Revitalize</div>
      </h1>
      <div class="rule"></div>
      <div class="brand">
        <div class="brand-name">Lumo Lodge</div>
        <div class="brand-tagline">Yoga - Meditation - Wellness</div>
      </div>
      <div class="yoga-photo" role="img" aria-label="Three women in stretching yoga poses"></div>
      <div class="visit-bar">Visit Us : www.lumolodge.example</div>
    </section>
  </main>
</body>
</html>
```